Verlane Area Planning Council Business Cards

We're looking for a business card design, simple as that. We're a local government agency that mainly performs building code enforcement, transportation planning, floodplain management, and GIS for Tobinet Parish in Louisiana, and other surround parishes. So you're not having to Google anything, GIS is, at it's core, mapping. Building Code Enforcement is just that, nothing more. Floodplain Management is to make sure the public is within what the government

Contact Information for Business Card

Our Address is

417 Merriwell Avenue
Corvane, TP 70000

Our phone is 5550192734
Our fax is 5550192739
Our website is www.vlpk.example
My email is dana@vlpk.example

Font styles to use
Serif
Sans Serif

Colors

Designer to choose colors to be used in the design.

Requirements
Must have
• I'm attaching our logo(several versions) that must be incorporated. The design should fit well with our existing logo. I can send photoshop files for our logo if needed. If possible, I'd like to be able to add names/info to each card for all of our employees once this is done.
Nice to have
• The State emblem is a bonus, and isn't specifically required.

```html
<!DOCTYPE html>
<html lang="en">
<head>
<meta charset="utf-8">
<title>Verlane Area Planning Council — Business Cards</title>
<link rel="stylesheet" href="https://fonts.googleapis.com/css2?family=Lato:wght@400;700;900&family=Montserrat:wght@300;600&display=swap">
<style>
  :root {
    --stage: #2b2b2d;
    --card-dark: #1b1a17;
    --pattern-a: #22241d;
    --pattern-b: #1a1c22;
    --card-light: #f7f7f5;
    --ink: #111111;
    --ink-soft: #3a3a3a;
    --white: #ffffff;
    --muted-light: #9a9a9a;
    --emblem: #244a8c;
    --logo-mark: #3aa845;
  }
  * { box-sizing: border-box; margin: 0; padding: 0; }
  html, body { width: 1200px; height: 1163px; overflow: hidden; }
  body {
    background: var(--stage);
    position: relative;
    font-family: "Lato", sans-serif;
  }
  .card {
    position: absolute;
    left: 150px;
    width: 900px;
    height: 514px;
    box-shadow: 0 18px 40px rgba(0,0,0,.45);
    overflow: hidden;
  }
  .card-back { top: 45px; background: var(--card-dark); }
  .card-front { top: 604px; background: var(--card-light); color: var(--ink); }

  .back-pattern {
    position: absolute; inset: 0;
    background: linear-gradient(135deg, var(--pattern-a), var(--card-dark) 45%, var(--pattern-b));
  }
  .back-brand {
    position: absolute; left: 150px; top: 160px;
    font-family: "Montserrat", sans-serif;
    color: var(--white);
  }
  .back-wordmark { font-weight: 600; font-size: 150px; letter-spacing: 2px; line-height: 1; }
  .back-name {
    font-weight: 300; font-size: 30px; color: var(--muted-light);
    margin-top: 10px; letter-spacing: 1px;
  }

  .front-logo {
    position: absolute; left: 60px; top: 55px;
    display: flex; align-items: center; gap: 18px;
  }
  .front-logo-mark { width: 80px; height: 80px; background: var(--logo-mark); }
  .front-logo-name {
    font-family: "Montserrat", sans-serif; font-weight: 600;
    font-size: 80px; line-height: 1; color: var(--ink);
  }
  .emblem {
    position: absolute; right: 60px; top: 50px;
    width: 130px; height: 130px; border-radius: 50%;
    background: var(--emblem);
    border: 6px solid #dfe4ee;
  }
  .org-details { position: absolute; left: 60px; top: 185px; }
  .org-title { font-size: 26px; font-weight: 400; margin-bottom: 18px; }
  .address { font-size: 26px; line-height: 1.2; color: var(--ink-soft); margin-bottom: 14px; }
  .address .org { color: var(--ink); }
  .contact-list { list-style: none; }
  .contact-list li {
    display: flex; align-items: center; gap: 18px;
    font-size: 26px; line-height: 1.28; color: var(--ink-soft);
  }
  .contact-list svg { width: 24px; height: 24px; fill: var(--ink); flex: none; }
  .person { position: absolute; right: 60px; top: 300px; text-align: right; }
  .person-name { font-size: 46px; font-weight: 900; }
  .person-role { font-size: 26px; color: var(--ink-soft); }
</style>
</head>
<body>
  <section class="card card-back">
    <div class="back-pattern" role="img" aria-label="Faint hexagon pattern with planning and mapping icons"></div>
    <div class="back-brand">
      <div class="back-wordmark">Verlane</div>
      <div class="back-name">Verlane Area Planning Council</div>
    </div>
  </section>

  <section class="card card-front">
    <div class="front-logo">
      <div class="front-logo-mark"></div>
      <div class="front-logo-name">Verlane</div>
    </div>
    <div class="emblem" role="img" aria-label="State emblem"></div>

    <div class="org-details">
      <p class="org-title">Verlane Area Planning Council</p>
      <p class="address"><span class="org">Verlane Area Planning Council</span><br>417 Merriwell Avenue<br>Corvane, TP 70000</p>
      <ul class="contact-list">
        <li><svg viewBox="0 0 24 24"><path d="M3 8c0-3 4-4 9-4s9 1 9 4v2h-5V8H8v2H3zM6 12h12l2 8H4z"/></svg>5550192734</li>
        <li><svg viewBox="0 0 24 24"><path d="M7 3h10v5H7zM3 9h18v8h-3v4H6v-4H3zm5 6v4h8v-4z"/></svg>5550192739</li>
        <li><svg viewBox="0 0 24 24"><path d="M2 5h20v14H2zm2 2v.5l8 6 8-6V7zm0 3v7h16v-7l-8 6z"/></svg>dana@vlpk.example</li>
        <li><svg viewBox="0 0 24 24"><path d="M12 2a10 10 0 1 0 0 20 10 10 0 0 0 0-20zm0 2c1.5 1.8 2.4 4.5 2.5 7h-5C9.6 8.5 10.5 5.8 12 4zM4.1 11a8 8 0 0 1 3.7-5.9A15 15 0 0 0 7.5 11zm0 2h3.4a15 15 0 0 0 .3 5.9A8 8 0 0 1 4.1 13zm5.4 0h5c-.1 2.5-1 5.2-2.5 7-1.5-1.8-2.4-4.5-2.5-7zm7 0h3.4a8 8 0 0 1-3.7 5.9 15 15 0 0 0 .3-5.9zm0-2a15 15 0 0 0-.3-5.9 8 8 0 0 1 3.7 5.9z"/></svg>www.vlpk.example</li>
      </ul>
    </div>

    <div class="person">
      <p class="person-name">Marlo Keene</p>
      <p class="person-role">Representative</p>
    </div>
  </section>
</body>
</html>
```